VEXO requires an exciting new business card

New business card required for VEXO. We are a new market research consultancy and want our brand to be approachable and be contemporary/modern, bold, uncomplicated/simple, and use friendly and easy to read fonts.

A draft website front page is attached to give you a feel (the pictures will be improved over the coming days).

The business card will be printed on 600gsm card, full colour both sides. The card is unique in that it allows one of four colours to be placed within the seam of the card (see http://uk.tarnix.com/products/halo/business-cards.html)

The logo has been designed in yellow on white, white on yellow, yellow on black and black on yellow - please select whichever you feel most appropriate from the attached document (please use the versions with the tagline). I think my preference is yellow on white for the front, and then yellow or black as the dominant colour on the back.

Telephone numbers will be given next week as they are now being finalised.

Thanks

Target Market(s)

Professionals in large corporates, such as Marketing Managers at Bravik, Fizzor Dune, Domacore etc.

Industry/Entity Type

Market Research

Requirements
Must have
• Greg Hallow QPMR
vexo
Level 4, 17 Ember St
Quindle Park
NSW 2087
Tel: 02 XXXX XXXX
Mob: XXXX XXXXXX
Email: greg@vexomr.com.au
Web: www.vexomr.com.au

```html
<!DOCTYPE html>
<html lang="en">
<head>
<meta charset="utf-8">
<title>VEXO business card</title>
<link rel="stylesheet" href="https://fonts.googleapis.com/css2?family=Montserrat:wght@400;500;600;700&display=swap">
<style>
  :root {
    --yellow: #f7bc1c;
    --white: #ffffff;
    --ink: #3a3a3c;
    --backdrop: #d9d9db;
    --shadow: rgba(0, 0, 0, 0.18);
  }
  * { margin: 0; padding: 0; box-sizing: border-box; }
  html, body {
    width: 1200px;
    height: 624px;
    overflow: hidden;
    background: var(--backdrop);
    font-family: "Montserrat", sans-serif;
  }
  .canvas {
    position: relative;
    width: 1200px;
    height: 624px;
  }
  .card {
    position: absolute;
    top: 163px;
    width: 520px;
    height: 298px;
    overflow: hidden;
    box-shadow: 0 6px 18px var(--shadow);
  }

  /* Back: contact side */
  .card-back {
    left: 50px;
    background: var(--white);
  }
  .card-back .wordmark {
    position: absolute;
    left: 40px;
    top: 32px;
    color: var(--yellow);
    font-weight: 600;
    font-size: 38px;
    letter-spacing: -0.5px;
    line-height: 1;
  }
  .person {
    position: absolute;
    left: 40px;
    top: 104px;
  }
  .person-name {
    color: var(--yellow);
    font-weight: 600;
    font-size: 17px;
    letter-spacing: 1px;
    text-transform: uppercase;
  }
  .person-title {
    color: var(--ink);
    font-weight: 600;
    font-size: 12px;
    letter-spacing: 0.5px;
    margin-top: 4px;
  }
  .contact-list {
    list-style: none;
    margin-top: 12px;
  }
  .contact-list li {
    display: flex;
    align-items: center;
    gap: 9px;
    color: var(--ink);
    font-weight: 600;
    font-size: 13px;
    line-height: 1;
    margin-bottom: 8px;
  }
  .contact-icon {
    width: 13px;
    height: 13px;
    flex: none;
  }
  .address-band {
    position: absolute;
    left: 0;
    right: 0;
    bottom: 18px;
    height: 34px;
    background: var(--yellow);
    color: var(--white);
    font-weight: 500;
    font-size: 13px;
    letter-spacing: 0.3px;
    display: flex;
    align-items: center;
    padding-left: 40px;
  }

  /* Front: brand side */
  .card-front {
    left: 630px;
    background: var(--yellow);
  }
  .front-curve {
    position: absolute;
    left: 0;
    top: 0;
  }
  .card-front .lockup {
    position: absolute;
    left: 300px;
    top: 76px;
    color: var(--white);
  }
  .card-front .wordmark {
    font-weight: 600;
    font-size: 52px;
    letter-spacing: -0.5px;
    line-height: 1;
  }
  .tagline {
    font-weight: 500;
    font-size: 11px;
    letter-spacing: 0.4px;
    margin-top: 6px;
    padding-left: 2px;
  }
</style>
</head>
<body>
<main class="canvas">

  <section class="card card-back" aria-label="Business card, contact side">
    <div class="wordmark">vexo</div>

    <div class="person">
      <p class="person-name">Greg Hallow</p>
      <p class="person-title">QPMR</p>
      <ul class="contact-list">
        <li>
          <svg class="contact-icon" viewBox="0 0 16 16" aria-hidden="true">
            <path fill="var(--yellow)" d="M3.5 1.5l2.6 0.4 1 3-1.7 1.4a9 9 0 0 0 4.3 4.3l1.4-1.7 3 1 0.4 2.6c-0.3 1-1.2 1.5-2.2 1.5C6.8 14 2 9.2 2 3.7c0-1 0.5-1.9 1.5-2.2z"/>
          </svg>
          02 7410 2958
        </li>
        <li>
          <svg class="contact-icon" viewBox="0 0 16 16" aria-hidden="true">
            <rect x="4" y="1" width="8" height="14" rx="1.5" fill="var(--yellow)"/>
            <rect x="5.3" y="2.8" width="5.4" height="8.6" fill="var(--white)"/>
            <circle cx="8" cy="13.1" r="0.8" fill="var(--white)"/>
          </svg>
          0412 846317
        </li>
        <li>
          <svg class="contact-icon" viewBox="0 0 16 16" aria-hidden="true">
            <rect x="1" y="3" width="14" height="10" rx="1" fill="var(--yellow)"/>
            <path d="M1.5 3.8L8 9l6.5-5.2" fill="none" stroke="var(--white)" stroke-width="1.3"/>
          </svg>
          greg@vexomr.com.au
        </li>
        <li>
          <svg class="contact-icon" viewBox="0 0 16 16" aria-hidden="true">
            <circle cx="8" cy="8" r="7" fill="var(--yellow)"/>
            <path d="M1.5 8h13M8 1.2c-2.5 3.8-2.5 9.8 0 13.6M8 1.2c2.5 3.8 2.5 9.8 0 13.6" fill="none" stroke="var(--white)" stroke-width="1"/>
          </svg>
          www.vexomr.com.au
        </li>
      </ul>
    </div>

    <div class="address-band">Level 4, 17 Ember St Quindle Park NSW 2087</div>
  </section>

  <section class="card card-front" aria-label="Business card, brand side">
    <svg class="front-curve" width="520" height="298" viewBox="0 0 520 298" aria-hidden="true">
      <path d="M0 0H120A149 149 0 0 1 120 298H0Z" fill="var(--white)"/>
    </svg>
    <div class="lockup">
      <div class="wordmark">vexo</div>
      <p class="tagline">market insight</p>
    </div>
  </section>

</main>
</body>
</html>
```